Parcel Nest products and services brochure.

I want a tri-fold brochure designed for my pack, ship, and print retail business. The brochure should highlight our most popular products and services (see attached for details). Please also incorporate our more detailed services as you see fit. I want to include something about stamps and that we offer drop-off services as well. All of the services don't need to be listed; maybe some of the main ones to fill out the design.
I’ve also included some images of the store that I’d like to incorporate throughout the design. The storefront photo should be featured prominently on the front cover. Please include our contact information, address, and hours on the back cover. Please crop and rotate the pictures to align them accordingly. Also, please display the carrier logos (QuikVan, TRX, NMLR) together somewhere appropriate and include the Boxwharf logo on the back cover.
Parcel Nest
4157 N Meadowlark Pkwy Ste. 208
Maple Ridge, TX 75493
Monday - Friday: 8 AM - 7 PM
Saturday: 9 AM - 2 PM
Please use the same red, blue, and white shades as our attached logo for the color scheme. I'd like the design to be catchy as it will be one of the first things I give to potential customers.
Thank you for your help!

```html
<!DOCTYPE html>
<html lang="en">
<head>
<meta charset="utf-8">
<title>Parcel Nest Tri-fold Brochure</title>
<link href="https://fonts.googleapis.com/css2?family=Archivo:ital,wght@1,900&family=Montserrat:wght@400;500;600;700;800&display=swap" rel="stylesheet">
<style>
:root{
  --red:#e3101e;
  --blue:#1a4fa0;
  --navy:#1b3f8f;
  --white:#ffffff;
  --ink:#2a2a2a;
  --bg:#dde3ef;
  --photo-sky:#9aa8b8;
  --photo-brick:#a88d70;
  --photo-dark:#2e2f33;
}
*{margin:0;padding:0;box-sizing:border-box}
html,body{width:1200px;height:2771px;overflow:hidden;background:var(--bg);font-family:"Montserrat",sans-serif;color:var(--ink)}
.spread{position:absolute;left:48px;width:1104px;height:853px;display:flex;box-shadow:0 10px 30px rgba(30,50,90,.18)}
.spread--outer{top:470px}
.spread--inner{top:1443px}
.panel{position:relative;width:368px;height:100%;overflow:hidden;background:var(--white)}
.photo{display:block;background:linear-gradient(180deg,var(--photo-sky) 0%,var(--photo-brick) 35%,var(--photo-brick) 60%,var(--photo-dark) 100%)}
.heading{font-weight:500;font-size:34px;color:var(--ink)}
.heading-rule{height:6px;background:var(--blue);margin-top:10px;width:300px}
.label{font-size:11px;font-weight:700;color:var(--red);letter-spacing:.02em;text-transform:uppercase;margin-bottom:6px}
.value{font-size:17px;font-weight:700;color:var(--blue);line-height:1.45}
.brand{display:flex;align-items:center;gap:10px;color:var(--white);font-weight:800;font-size:24px;letter-spacing:.02em}
.brand-dot{width:26px;height:26px;border-radius:50%;background:var(--white)}
/* outer left */
.why-photo{height:460px}
.why{background:var(--blue);color:var(--white);padding:22px 32px;height:393px;font-size:16px;line-height:1.6}
.why h3{font-size:19px;font-weight:700;margin-bottom:14px}
.why ul{list-style:none;margin:12px 0 16px 18px}
.why li{font-weight:700;font-size:16px;position:relative;padding-left:20px;margin-bottom:4px}
.why li::before{content:"";position:absolute;left:0;top:8px;width:9px;height:9px;border-radius:50%;background:var(--red)}
/* outer middle */
.contact{padding:28px 32px}
.contact-block{margin-top:34px}
.partners{position:absolute;left:32px;bottom:80px;display:flex;flex-direction:column;gap:22px}
.partner{display:flex;align-items:center;gap:12px;font-weight:700;font-size:22px;color:var(--navy)}
.partner-badge{width:56px;height:56px;background:#3a2318}
.partner-box{width:28px;height:28px;background:var(--navy)}
.web-rule{position:absolute;left:32px;right:32px;bottom:52px;height:5px;background:var(--red)}
.web{position:absolute;left:32px;bottom:20px;font-size:13px;letter-spacing:.32em;color:var(--ink)}
/* outer right */
.cover-bar{height:82px;background:var(--blue);display:flex;align-items:center;justify-content:center}
.cover-title{font-family:"Archivo",sans-serif;font-style:italic;font-weight:900;font-size:46px;line-height:1.12;color:var(--blue);text-align:center;padding-top:30px;height:208px;text-transform:uppercase}
.cover-photo{height:392px}
.cover-stripe{height:44px;background:var(--blue)}
.cover-address{background:var(--red);color:var(--white);font-weight:700;font-size:17px;line-height:1.3;padding:18px 34px;height:127px;text-transform:uppercase}
/* inner left */
.about{background:var(--red);color:var(--white);padding:28px 34px}
.about .heading{color:var(--white)}
.about .heading-rule{background:var(--white)}
.about-lead{font-size:16px;line-height:1.45;margin-top:34px}
.about p{font-size:13.5px;line-height:1.55;margin-top:18px}
.about-mark{position:absolute;left:0;right:0;bottom:0;height:300px;background:var(--red)}
/* services */
.services{padding:28px 32px 0}
.service-list{margin-top:26px}
.service{position:relative;height:91px;padding-top:38px}
.service-name{font-size:15px;font-weight:600;text-transform:uppercase;color:var(--ink);padding-bottom:4px;border-bottom:2px solid var(--red)}
.service-icon{position:absolute;right:4px;top:10px;width:34px;height:34px;border-radius:6px;background:linear-gradient(135deg,var(--blue),var(--red))}
.bullets{display:grid;grid-template-columns:repeat(3,1fr);font-size:11px;color:var(--ink);margin-top:6px;gap:2px 4px}
.bullets span::before{content:"";display:inline-block;width:5px;height:5px;border-radius:50%;background:var(--red);margin-right:6px;vertical-align:middle}
.services-right{padding:28px 28px 0;padding-top:106px}
.dropoff{position:absolute;left:0;right:0;bottom:0;height:313px;background:var(--blue);color:var(--white);padding:22px 34px}
.dropoff h4{font-size:17px;font-weight:600;text-transform:uppercase;padding-bottom:4px;border-bottom:2px solid var(--red);margin-bottom:12px}
.dropoff p{font-size:14px;line-height:1.55;margin-bottom:26px}
</style>
</head>
<body>

<section class="spread spread--outer">
  <div class="panel">
    <div class="photo why-photo" role="img" aria-label="Photo of the Parcel Nest storefront with shop sign and awnings"></div>
    <div class="why">
      <h3>WHY CHOOSE PARCEL NEST?</h3>
      <p>At Parcel Nest, we make your life easier by providing:</p>
      <ul>
        <li>Photos</li>
        <li>Affordable Prices</li>
        <li>Convenient One-Stop Solutions</li>
      </ul>
      <p>Whether you're shipping a package, printing a project, or need office supplies, we're here to help—quickly and efficiently.</p>
    </div>
  </div>

  <div class="panel contact">
    <h2 class="heading">Contact Us</h2>
    <div class="heading-rule"></div>
    <div class="contact-block">
      <div class="label">Address</div>
      <div class="value">4157 N Meadowlark Pkwy<br>Ste. 208<br>Maple Ridge, TX 75493</div>
    </div>
    <div class="contact-block">
      <div class="label">Business Hours</div>
      <div class="value">Monday - Friday: 8 AM - 7 PM<br>Saturday: 9 AM - 2 PM</div>
    </div>
    <div class="contact-block">
      <div class="label">Phone</div>
      <div class="value">555-410-0187</div>
    </div>
    <div class="partners">
      <div class="partner"><span class="partner-badge"></span>TRX</div>
      <div class="partner">QuikVan</div>
      <div class="partner"><span class="partner-box"></span>NMLR</div>
    </div>
    <div class="web-rule"></div>
    <div class="web">WWW.PARCELNEST.COM</div>
  </div>

  <div class="panel">
    <div class="cover-bar"><div class="brand"><span class="brand-dot"></span>PARCEL NEST</div></div>
    <h1 class="cover-title">The Pack,<br>Ship &amp; Print<br>Experts</h1>
    <div class="photo cover-photo" role="img" aria-label="Front view of the Parcel Nest storefront entrance"></div>
    <div class="cover-stripe"></div>
    <div class="cover-address">4157 N Meadowlark Pkwy,<br>Ste. 208<br>Maple Ridge, TX</div>
  </div>
</section>

<section class="spread spread--inner">
  <div class="panel about">
    <h2 class="heading">About Us</h2>
    <div class="heading-rule"></div>
    <p class="about-lead">Parcel Nest located at <b>4157 N Meadowlark Pkwy Ste. 208, Maple Ridge, TX</b> is the go-to resource for all your packing, shipping, printing, and business service needs.</p>
    <p>Our team of professionally trained experts delivers Super-Star Customer Care, ensuring you get the right products and services at the best price—in a single, quick visit.</p>
    <p>We specialize in packing and shipping (almost) anything to (almost) anywhere in the world, but our services go far beyond that. As Maple Ridge's premier copy, print, and document services center, Parcel Nest handles everything from large-scale printing to small projects, in black and white or color.</p>
    <div class="about-mark"></div>
  </div>

  <div class="panel services">
    <h2 class="heading">Services</h2>
    <div class="heading-rule"></div>
    <div class="service-list">
      <div class="service"><div class="service-name">Mailing &amp; Shipping</div><span class="service-icon" role="img" aria-label="Envelope icon"></span><div class="bullets"><span>NMLR</span><span>QuikVan</span><span>TRX</span></div></div>
      <div class="service"><div class="service-name">Mailbox Rentals</div><span class="service-icon" role="img" aria-label="Mailbox icon"></span></div>
      <div class="service"><div class="service-name">Package Receiving</div><span class="service-icon" role="img" aria-label="Package in hand icon"></span></div>
      <div class="service"><div class="service-name">Office Services</div><span class="service-icon" role="img" aria-label="Fax machine icon"></span><div class="bullets"><span>Scan &amp; Fax</span><span>Laminating</span><span>Binding</span></div></div>
      <div class="service"><div class="service-name">Office Supplies</div><span class="service-icon" role="img" aria-label="Office supplies icon"></span></div>
      <div class="service"><div class="service-name">Packing Material</div><span class="service-icon" role="img" aria-label="Box icon"></span></div>
      <div class="service"><div class="service-name">Printing Services</div><span class="service-icon" role="img" aria-label="Printer icon"></span><div class="bullets"><span>Photos</span><span>Banners</span><span>Flyers</span><span>Brochures</span><span>Signs</span><span>Blueprints</span><span>Invitations</span><span>Copies</span><span>Business Card</span></div></div>
    </div>
  </div>

  <div class="panel services-right">
    <div class="service"><div class="service-name">Passport Photos</div><span class="service-icon" role="img" aria-label="ID photo icon"></span></div>
    <div class="service"><div class="service-name">Notary Public</div><span class="service-icon" role="img" aria-label="Notarized document icon"></span></div>
    <div class="service"><div class="service-name">Gift Wrapping</div><span class="service-icon" role="img" aria-label="Gift box icon"></span></div>
    <div class="service"><div class="service-name">Greeting Cards</div><span class="service-icon" role="img" aria-label="Greeting card icon"></span></div>
    <div class="service"><div class="service-name">Unique Gifts &amp; More</div><span class="service-icon" role="img" aria-label="Heart gift icon"></span></div>
    <div class="dropoff">
      <h4>Drop-Off Services</h4>
      <p>Save time with our QuikVan, TRX, and NMLR drop-off services! Just bring your pre-labeled packages, and we'll handle the rest—no extra charge.</p>
      <h4>Stamps Available</h4>
      <p>Need stamps? Skip the Post Office! We offer regular and special-order stamps for all your mailing needs.</p>
    </div>
  </div>
</section>

</body>
</html>
```